Investment Company Business Card Design

We need a Business Card design for a new company based in Boston called "Velm Investment". We are cooperating with local real estate and construction companies. Our company is very actively and aggressively acquiring primarily residential investment properties either to buy and hold long term or for purposes or renovating and repositioning for re-sale in the market. In addition, we undertake some development projects and acquisitions as opportunities present themselves. the final design should contains information about “Velm" the river boat. we are tenacious, indomitable, and the business have a favorable wind throughout the voyage for all our investment.
sample Info. on Design:
Tusa Merrick
CEO
555-xxx-xxxx
418 Harlow St. Suite 507, Carvale, MA 02190
Please provide a template also, that we can edit the info later.
Reason: i just got new LOGO Design attached will be use in Business Card Design.
Construction

```html
<!DOCTYPE html>
<html lang="en">
<head>
<meta charset="utf-8">
<title>Velm Investment Business Card</title>
<link rel="stylesheet" href="https://fonts.googleapis.com/css2?family=Questrial&display=swap">
<style>
  :root {
    --paper: #ffffff;
    --bronze: #857650;
    --ink: #58585a;
    --rule: #6d6d6d;
    --edge: #4a4a4a;
  }
  * { margin: 0; padding: 0; box-sizing: border-box; }
  html, body {
    width: 1018px;
    height: 1200px;
    overflow: hidden;
    background: var(--paper);
    font-family: "Questrial", "Century Gothic", sans-serif;
  }
  .sheet { position: relative; width: 1018px; height: 1200px; }

  .card-shape { position: absolute; left: 0; top: 0; }

  .front-divider {
    position: absolute;
    left: 523px; top: 242px;
    width: 2px; height: 195px;
    background: var(--rule);
  }
  .contact {
    position: absolute;
    left: 557px; top: 238px;
    color: var(--ink);
    white-space: nowrap;
  }
  .contact .name {
    font-size: 23px;
    font-weight: 700;
    letter-spacing: 0.3px;
    color: var(--bronze);
    line-height: 28px;
  }
  .contact .role { font-size: 21px; line-height: 29px; }
  .contact .phone { font-size: 24px; line-height: 29px; }
  .contact .address { font-size: 24px; line-height: 31px; margin-top: 52px; }

  .brand {
    position: absolute;
    display: flex;
    align-items: center;
    gap: 12px;
    white-space: nowrap;
  }
  .brand .mark { border-radius: 50%; flex: none; }
  .brand-front { left: 200px; top: 328px; color: var(--bronze); font-size: 30px; letter-spacing: 1px; }
  .brand-front .mark { width: 18px; height: 18px; background: var(--bronze); }
  .brand-back { left: 456px; top: 858px; color: var(--paper); font-size: 40px; letter-spacing: 1.5px; }
  .brand-back .mark { width: 24px; height: 24px; background: var(--paper); }
</style>
</head>
<body>
<main class="sheet">
  <svg class="card-shape" width="1018" height="1200" aria-hidden="true">
    <path d="M333.5 116.5 H907.5 V562.5 H333.5 A223 223 0 0 1 333.5 116.5 Z"
          fill="none" stroke="var(--edge)" stroke-width="1"/>
    <path d="M110 655 H685 A223.5 223.5 0 0 1 685 1102 H110 Z" fill="var(--bronze)"/>
    <g stroke="var(--paper)" stroke-width="1.6">
      <line x1="151" y1="935" x2="553" y2="935"/>
      <line x1="252" y1="943" x2="576" y2="943"/>
      <line x1="431" y1="953" x2="602" y2="953"/>
    </g>
  </svg>

  <div class="brand brand-front"><span class="mark"></span>VELM INVEST</div>
  <div class="front-divider"></div>
  <section class="contact">
    <p class="name">TUSA MERRICK</p>
    <p class="role">CEO</p>
    <p class="phone">555.014.2290</p>
    <p class="address">418 Harlow St. Suite 507,<br>Carvale, MA 02190</p>
  </section>

  <div class="brand brand-back"><span class="mark"></span>VELM INVEST</div>
</main>
</body>
</html>
```